Your complete Gardening and lawn maintenance, Horticultural care. (to be on card)
We are looking at using a logo of a tree, with a recycling emblem circling the tree. The colors of choice, are burnt oranges and olive greens. Presented; simple to the eye, yet catchy to the clients in a eco-friendly way. We have uploaded a design for you to look at just to give a rough idea, you can use that or create your own ideas or play around with a mixture.

Target Market(s)

Home owners, businesses, real estates.

Industry/Entity Type

Recycling

Contact Information for Business Card

Name: Colin Breversted
Phone: 0438159027
Email: brightmossyards@mailbarn.net

Logo Text

Bright-Moss Yards

Logo styles of interest
Emblem Logo
Pictorial/Combination Logo
Abstract Logo
Requirements
Must have
• Business name: Bright-Moss Yards
and slogan : Your complete Gardening and lawn maintenance, Horticultural care

```html
<!DOCTYPE html>
<html lang="en">
<head>
<meta charset="utf-8">
<title>Bright-Moss Yards – Business Card</title>
<link rel="stylesheet" href="https://fonts.googleapis.com/css2?family=Josefin+Sans:wght@400;600&display=swap">
<style>
  :root {
    --backdrop: #e6e7e8;
    --burnt-orange: #d2582b;
    --olive: #808236;
    --divider: #ffffff;
    --ink-light: #ffffff;
  }
  html, body {
    margin: 0;
    padding: 0;
    width: 1200px;
    height: 1000px;
    overflow: hidden;
    background: var(--backdrop);
    font-family: "Josefin Sans", "Helvetica Neue", Arial, sans-serif;
  }
  .business-card {
    position: absolute;
    left: 230px;
    top: 287px;
    width: 740px;
    height: 426px;
    display: flex;
    background: var(--divider);
  }
  .brand-panel {
    width: 288px;
    height: 100%;
    box-sizing: border-box;
    padding: 0 24px;
    background: var(--burnt-orange);
    color: var(--ink-light);
    display: flex;
    flex-direction: column;
    align-items: center;
    justify-content: center;
    text-align: center;
  }
  .brand-dot {
    width: 120px;
    height: 120px;
    border-radius: 50%;
    background: var(--ink-light);
  }
  .brand-name {
    margin: 18px 0 0;
    font-weight: 600;
    font-size: 24px;
    line-height: 1.2;
    letter-spacing: 0.5px;
  }
  .brand-slogan {
    margin: 10px 0 0;
    font-weight: 400;
    font-size: 14px;
    line-height: 1.4;
    letter-spacing: 0.2px;
  }
  .card-divider {
    width: 9px;
    height: 100%;
    background: var(--divider);
  }
  .contact-panel {
    flex: 1;
    height: 100%;
    background: var(--olive);
    color: var(--ink-light);
    position: relative;
  }
  .contact-name {
    position: absolute;
    left: 36px;
    top: 158px;
    margin: 0;
    font-weight: 600;
    font-size: 33px;
    letter-spacing: 0.3px;
    white-space: nowrap;
  }
  .contact-line {
    position: absolute;
    left: 36px;
    margin: 0;
    font-weight: 600;
    font-size: 20px;
    letter-spacing: 0.4px;
    white-space: nowrap;
  }
  .contact-phone { top: 208px; }
  .contact-email { top: 247px; }
</style>
</head>
<body>
  <main class="business-card">
    <section class="brand-panel">
      <div class="brand-dot"></div>
      <p class="brand-name">Bright-Moss Yards</p>
      <p class="brand-slogan">Your complete Gardening and lawn maintenance, Horticultural care</p>
    </section>
    <div class="card-divider"></div>
    <section class="contact-panel">
      <h1 class="contact-name">Colin Breversted</h1>
      <p class="contact-line contact-phone">P: 0438159027</p>
      <p class="contact-line contact-email">E: brightmossyards@mailbarn.net</p>
    </section>
  </main>
</body>
</html>
```